High-End Medical Center Website Design Project

This design is part of a well thought-out project by an experienced project manager / developer. The approved wireframe is attached. Creative interpretations / suggestions based on the layout encouraged.

The design is for a new state-of-the-art medical center located in Dallas, Texas. The target audience would likely be individuals (approx. 60% female /40% male) who are the healthcare decision-makers for their families. They would likely have insurance and be inclined to seek out top-quality care.

Potential clients would choose this client over others in their industry because the medical center is physician owned, meaning it is patient-focused rather than profit-focused. The facility is brand new, featuring the latest technology. (This includes an amazing waiting room featuring WiFi and docking stations.) The physicians are hand-picked by referral only.

The look of the site should be extremely clean. We are going for a well-organized, professional look with a bit of a warm glow (interpret that however you like). Use crisp corners and the colors in the logo.

Think modern, clean with some great use of color / font.

We can get lovely photography of the medical center once construction is complete. Feel free to use an "example image" behind the Featured Area ("Physician Owned. Patient-Focused") if you like. We are open to ideas.

ONE CHANGE REQUESTED IN THE WIREFRAME:

Remove the "Connect" 1/4 page footer area and replace with a quick contact form. You may swap the "Locations" area with the form if desired. Put social media icons at the top left of the page in the top header area.

(Note: Please use social media icons that match the design rather than standard icons. We preferred not placing the icons at the top, but the client requested this. Let's not bring more attention to them than necessary.)
Updates

We're custom programming this site, so there's no need to base it on a template. Also, we would prefer not to use typical "seen everywhere" stock images.Thanks.

Industry/Entity Type

Construction

Requirements
Must have
• Follow the wireframe. This has been approved.
Nice to have
• Examples of what hover states, links or dropdowns might look like.

```html
<!DOCTYPE html>
<html lang="en">
<head>
<meta charset="utf-8">
<title>NOVA Medical Center</title>
<link href="https://fonts.googleapis.com/css2?family=Arimo:wght@400;700&family=Ubuntu:wght@400;500;700&display=swap" rel="stylesheet">
<style>
:root{
  --top:#137aa6;
  --navy:#0c4886;
  --navy-dark:#0a3566;
  --sky:#6aa6c4;
  --teal:#1d7fa0;
  --heading:#1a4f86;
  --text:#333;
  --grey-band:#eeeeee;
  --rule:#d9d9d9;
}
*{margin:0;padding:0;box-sizing:border-box}
html,body{width:852px;height:1200px;overflow:hidden;background:#fff}
body{position:relative;font-family:"Arimo",Arial,sans-serif;color:var(--text)}
.abs{position:absolute}
.topbar{left:0;top:0;width:852px;height:25px;background:var(--top)}
.topbar .call{right:102px;top:7px;color:#fff;font-size:9px;font-weight:700;display:flex;align-items:center;gap:5px}
.social-top{left:100px;top:5px;display:flex;gap:6px}
.social-top a{width:15px;height:15px;border-radius:50%;background:rgba(255,255,255,.22);display:flex;align-items:center;justify-content:center}
.social-top a:hover{background:rgba(255,255,255,.45)}
.brand{left:100px;top:50px;height:28px;display:flex;align-items:center;gap:6px;font-family:"Ubuntu",sans-serif;font-weight:700;font-size:22px;color:var(--navy);letter-spacing:1px}
.brand .mark{width:22px;height:22px;background:var(--navy)}
.search{left:608px;top:53px;width:143px;height:26px;border:1px solid #ccc;border-radius:4px;background:#f6f6f6;font-size:8px;padding:8px 0 0 6px}
.search svg{position:absolute;right:8px;top:7px}
.nav{left:99px;top:106px;width:653px;height:38px;background:linear-gradient(#1059a0,var(--navy-dark));font-size:9.5px;color:#fff}
.nav a{color:#fff;text-decoration:none;display:block;line-height:38px;position:absolute}
.nav a.active{background:var(--sky);padding:0 21px}
.nav a:hover{color:#cfe6f2}
.hero{left:99px;top:163px;width:653px;height:281px;background:linear-gradient(#2e5fa8 0%,#6f95c8 35%,#c9d3dc 55%,#8a8f96 78%,#4a4a4f 100%)}
.hero .caption{left:0;top:216px;width:216px;height:31px;background:rgba(11,53,102,.92);color:#fff;font-size:10.5px;font-weight:700;line-height:31px;padding-left:10px;word-spacing:2px}
.hero .dots{left:13px;top:253px;display:flex;gap:6px}
.hero .dots i{width:9px;height:9px;border-radius:50%;background:#fff;display:block}
.hero .dots i:first-child{background:var(--top)}
.feature{width:200px;text-align:center}
.feature .ring{width:85px;height:85px;border:1px solid #bbb;border-radius:50%;margin:0 auto;display:flex;align-items:center;justify-content:center}
.feature h3{font-family:"Ubuntu",sans-serif;font-weight:500;color:var(--heading);font-size:13px;margin-top:12px}
.feature p{font-size:8.6px;line-height:11px;margin:7px auto 0;width:166px;color:#222}
.rule{left:164px;top:645px;width:524px;height:1px;background:var(--rule)}
.apart-title{left:100px;top:709px;font-family:"Ubuntu",sans-serif;font-weight:500;font-size:12.5px;color:var(--heading)}
.apart h4{font-family:"Ubuntu",sans-serif;font-weight:500;color:var(--teal);font-size:12px}
.apart p{font-size:8px;line-height:13.5px;margin-top:10px;width:135px}
.vline{width:1px;height:78px;top:672px;background:var(--rule)}
.band{left:0;top:787px;width:852px;height:179px;background:var(--grey-band)}
.photo{left:76px;top:817px;width:164px;height:125px;background:linear-gradient(90deg,#e6ecf1,#cfd8e0 50%,#eef1f4);border:1px solid #ddd}
.story h2,.testi h2{font-family:"Ubuntu",sans-serif;font-weight:500;color:var(--heading);font-size:13px}
.story p{font-size:7.8px;line-height:10.7px;width:226px;margin-top:9px;text-align:justify}
.btn{display:inline-block;background:var(--navy);color:#fff;font-family:"Ubuntu",sans-serif;font-weight:500;font-size:9px;padding:5px 11px;border-radius:3px;margin-top:13px;text-decoration:none}
.btn:hover{background:var(--top)}
.testi .sub{font-size:8px;color:var(--teal);margin-top:10px;font-family:"Ubuntu",sans-serif}
.testi p{font-size:7.8px;line-height:10.7px;width:222px;margin-top:12px;text-align:justify}
.testi .by{font-family:"Ubuntu",sans-serif;font-size:8.5px;color:var(--heading);font-weight:500;margin-top:12px}
.quote{font-family:Georgia,serif;color:#999;font-size:16px}
.footer{left:0;top:975px;width:852px;height:191px;background:linear-gradient(#0f58a2,#0b3566);color:#fff}
.footer h5{font-size:10.5px;font-weight:700;position:absolute}
.item{position:absolute;display:flex;gap:7px}
.thumb{width:53px;height:48px;background:linear-gradient(#c9d4de,#6d84a0);border:1px solid #fff}
.item b{font-size:7.3px;display:block;margin-top:8px}
.item span{font-size:7.8px;line-height:10.5px;display:block;margin-top:7px;width:110px}
.contact-form{left:441px;top:32px;width:168px}
.field{height:19px;background:#fff;color:#777;font-size:7px;padding:5px 6px;margin-bottom:6px}
.field.message{height:38px}
.send{left:565px;top:1140px}
.send-btn{width:46px;height:19px;background:#fff;color:var(--navy);font-size:9.5px;font-weight:700;text-align:center;line-height:19px;font-family:"Ubuntu",sans-serif;margin-left:auto}
.wait{left:632px;top:35px;width:40px;height:31px;background:#8a8a8a;border-radius:2px;font-size:10.5px;text-align:center;line-height:31px}
.ftext{font-size:7.8px;line-height:10.5px}
.bottom{left:0;top:1166px;width:852px;height:34px;background:#0d3f6e;color:#fff;font-size:8px}
.bottom a{color:#fff;text-decoration:none}
</style>
</head>
<body>

<div class="abs topbar">
  <div class="abs social-top">
    <a href="#" aria-label="Social profile"><svg width="8" height="7" viewBox="0 0 8 7"><path d="M1 1 H7 V5 H3 L1.5 6.5 V5 H1Z" fill="#fff"/></svg></a>
    <a href="#" aria-label="Social profile"><svg width="8" height="8" viewBox="0 0 8 8"><circle cx="2" cy="4" r="1.2" fill="#fff"/><circle cx="6" cy="1.8" r="1.2" fill="#fff"/><circle cx="6" cy="6.2" r="1.2" fill="#fff"/><path d="M2 4 L6 1.8 M2 4 L6 6.2" stroke="#fff" stroke-width=".8"/></svg></a>
    <a href="#" aria-label="Email"><svg width="8" height="6" viewBox="0 0 8 6"><rect x=".5" y=".5" width="7" height="5" fill="none" stroke="#fff" stroke-width=".9"/><path d="M.5 .5 L4 3.3 L7.5 .5" fill="none" stroke="#fff" stroke-width=".9"/></svg></a>
  </div>
  <div class="abs call">
    <svg width="10" height="8" viewBox="0 0 10 8"><path d="M1 3 Q5 0 9 3 L8 4 L6 3 L6 2 Q5 1.6 4 2 L4 3 L2 4Z M2 5 H8 V8 H2Z" fill="#fff"/></svg>
    Call Us : (555) 018- 2940
  </div>
</div>

<div class="abs brand"><span class="mark"></span>NOVA MEDICAL CENTER</div>

<div class="abs search">Search
  <svg width="11" height="11" viewBox="0 0 11 11"><circle cx="4.5" cy="4.5" r="3.3" fill="none" stroke="#222" stroke-width="1.6"/><path d="M7 7 L10 10" stroke="#222" stroke-width="2"/></svg>
</div>

<nav class="abs nav">
  <a class="active" href="#" style="left:34px">WHY NOVA</a>
  <a href="#" style="left:153px">PHYSICIANS</a>
  <a href="#" style="left:260px">SPECIALITIES</a>
  <a href="#" style="left:373px">INFO</a>
  <a href="#" style="left:444px">LOCATIONS</a>
  <a href="#" style="left:548px">CONTACT</a>
</nav>

<section class="abs hero" role="img" aria-label="Photograph of the modern medical center building under a blue sky">
  <div class="abs caption">Physician Owned &nbsp; Patient Focused</div>
  <div class="abs dots"><i></i><i></i><i></i></div>
</section>

<div class="abs feature" style="left:97px;top:476px">
  <div class="ring">
    <svg width="38" height="38" viewBox="0 0 38 38"><rect width="38" height="38" rx="3" fill="#1c9aa8"/><path d="M6 19 L19 8 L32 19 M10 17 V30 H28 V17" fill="none" stroke="#fff" stroke-width="3"/><path d="M19 18 V27 M14.5 22.5 H23.5" stroke="#fff" stroke-width="3"/></svg>
  </div>
  <h3>Physicians</h3>
  <p>The standard chunk of Lorem Ipsum used is reproduced below for those interested. theexact original</p>
</div>
<div class="abs feature" style="left:328px;top:476px">
  <div class="ring">
    <svg width="38" height="38" viewBox="0 0 38 38"><rect width="38" height="38" rx="3" fill="#3f63a6"/><path d="M9 19 L16 26 L29 12" fill="none" stroke="#fff" stroke-width="4"/></svg>
  </div>
  <h3>Physicians</h3>
  <p>The standard chunk of Lorem Ipsum used is reproduced below for those interested. theexact original</p>
</div>
<div class="abs feature" style="left:550px;top:476px">
  <div class="ring"><span style="font-family:Ubuntu,sans-serif;font-size:44px;color:#1a3f73">?</span></div>
  <h3>Physicians</h3>
  <p>The standard chunk of Lorem Ipsum used is reproduced below for those interested. theexact original</p>
</div>

<div class="abs rule"></div>

<div class="abs apart-title">WHAT SETS UP APART</div>
<div class="abs apart" style="left:265px;top:676px"><h4>Technology</h4><p>The standard chunk of Lorem Ipsum used is reproduced below for those interested. theexact original</p></div>
<div class="abs vline" style="left:418px"></div>
<div class="abs apart" style="left:439px;top:676px"><h4>Quality Of Core</h4><p>The standard chunk of Lorem Ipsum used is reproduced below for those interested. theexact original</p></div>
<div class="abs vline" style="left:590px"></div>
<div class="abs apart" style="left:610px;top:676px"><h4>Patience Experience</h4><p>The standard chunk of Lorem Ipsum used is reproduced below for those interested. theexact original</p></div>

<section class="abs band"></section>
<div class="abs photo" role="img" aria-label="Photograph of three medical staff members in a bright clinic"></div>
<div class="abs story" style="left:261px;top:817px">
  <h2>Survived Not Only Five Centuries</h2>
  <p>"Lorem ipsum dolor sit amet, consectetur adipisicing elit, sed do eiusmod tempor incididunt ut labore et dolore magna aliqua. Ut enim ad minim veniam, quis nostrud exercitation cillum dolore eu fugiat nulla pariatur. Excepteur sint occaecat cupidatat non proident, sunt in culpa qui officia deserunt mollit anim id est laborum."</p>
  <a class="btn" href="#">READ MORE</a>
</div>
<div class="abs testi" style="left:520px;top:816px">
  <h2>Testimonials</h2>
  <div class="sub">LOREM IPSUM</div>
  <p>"Lorem ipsum dolor sit amet, consectetur adipisicing elit, sed do eiusmod tempor incididunt ut labore et dolore magna aliqua. Ut enim</p>
  <div class="by">by J. Ellison.</div>
</div>
<div class="abs quote" style="left:505px;top:855px">&ldquo;</div>
<div class="abs quote" style="left:737px;top:898px">&rdquo;</div>

<footer class="abs footer">
  <h5 style="left:78px;top:15px">News</h5>
  <div class="item" style="left:76px;top:37px"><div class="thumb" role="img" aria-label="Portrait photo of a doctor"></div><div><b>LOREM IPSUM</b><span>"Lorem ipsum dolor sit amet, consectetur adipisicing elit</span></div></div>
  <div class="item" style="left:76px;top:113px"><div class="thumb" role="img" aria-label="Portrait photo of a staff member"></div><div><b>LOREM IPSUM</b><span>"Lorem ipsum dolor sit amet, consectetur adipisicing elit</span></div></div>

  <h5 style="left:261px;top:15px">Blog</h5>
  <div class="item" style="left:259px;top:37px"><div class="thumb" role="img" aria-label="Photo of a doctor at work"></div><div><b>LOREM IPSUM</b><span>"Lorem ipsum dolor sit amet, consectetur adipisicing elit</span></div></div>
  <div class="item" style="left:259px;top:113px"><div class="thumb" role="img" aria-label="Photo of a nurse"></div><div><b>LOREM IPSUM</b><span>"Lorem ipsum dolor sit amet, consectetur adipisicing elit</span></div></div>

  <h5 style="left:441px;top:14px">Quick Contact</h5>
  <form class="abs contact-form">
    <div class="field">Your name</div>
    <div class="field">Your email address</div>
    <div class="field">Phone number</div>
    <div class="field message">Your message</div>
    <div class="send-btn">SUBMIT</div>
  </form>

  <h5 style="left:622px;top:14px">Average Wait Time</h5>
  <div class="abs wait">9 MIN</div>
  <div class="abs ftext" style="left:622px;top:75px;width:120px">"Lorem ipsum dolor sit amet, consectetur adipisicing elit</div>
  <h5 style="left:623px;top:108px">Locations</h5>
  <div class="abs ftext" style="left:623px;top:127px;font-size:8px;line-height:10.6px">no : 15,street name .<br>city, contry<br>zip code :1111</div>
</footer>

<div class="abs bottom">
  <span class="abs" style="left:77px;top:14px">Copyrights @ 2013 All Rights Reserved</span>
  <span class="abs" style="left:630px;top:16px"><a href="#">SITEMAP</a> &nbsp;|&nbsp; <a href="#">PRIVACY POLICY</a></span>
</div>

</body>
</html>
```